New design for our website – modern, elegant, and customer-focused

We want to redesign our website, www.kalmenstrand.se, to create a completely new look that reflects the high quality of our products and services. We are seeking assistance in developing a modern, clean, and user-friendly web experience in Flatsome that strengthens our brand and makes it easier for customers to find the right solutions. Our goal is to enhance the design, functionality, and overall impression to better meet today’s expectations and demands.

Target Market(s)

swimmingpool & spa

Industry/Entity Type

Poolbusiness

Coding

Coded - Design and coding required

Number of Pages Required

1 page

Font styles to use
Other font styles liked:
• HaboroSoft

Requirements
Must have
• We working in Flatsome
Nice to have
• From dream to reality – swimming pools that transform your garden into a place of life and enjoyment.
Should not have
• Nice look

```html
<!DOCTYPE html>
<html lang="en">
<head>
<meta charset="utf-8">
<title>Kalmenstrand – Swimming Pools &amp; Spa</title>
<link href="https://fonts.googleapis.com/css2?family=Poppins:wght@300;400;500;600;700&display=swap" rel="stylesheet">
<style>
:root{
  --blue:#1f6fb5;
  --blue-dark:#0f4f8c;
  --navy:#0d1627;
  --ink:#1b1f2a;
  --muted:#5b6272;
  --line:#d7dce4;
  --teal-dark:#0e3a4c;
  --teal:#1b6a83;
  --white:#ffffff;
  --star:#f2b630;
}
*{box-sizing:border-box;margin:0;padding:0}
html,body{width:1200px;height:4699px;overflow:hidden}
body{font-family:'Poppins',sans-serif;color:var(--ink);background:var(--white);position:relative}
.abs{position:absolute}
section,header,footer{position:absolute;left:0;width:1200px}
.photo{position:absolute;border-radius:14px;overflow:hidden}
/* top bar */
.topbar{top:0;height:37px;background:linear-gradient(90deg,#1a6cb0,#2a86c9);color:#fff;font-size:10px}
.topbar .hours{left:150px;top:12px}
.social{display:flex;gap:10px}
.social span{width:18px;height:18px;border-radius:50%;background:#fff;display:block}
.topbar .social{position:absolute;right:150px;top:9px}
/* nav */
.nav{top:37px;height:60px;background:#fff;border-bottom:1px solid #e6e9ee}
.brand{position:absolute;display:flex;align-items:center;gap:8px;font-weight:600;color:var(--blue)}
.nav .brand{left:150px;top:17px;font-size:20px}
.brand i{display:block;width:10px;height:10px;border-radius:50%;background:currentColor}
.nav ul{position:absolute;left:400px;top:22px;display:flex;gap:38px;list-style:none;font-size:12px;font-weight:500}
.btn{position:absolute;display:flex;align-items:center;justify-content:center;border-radius:6px;font-weight:600;font-size:12px}
.btn-blue{background:linear-gradient(180deg,#2a80c6,#155a9a);color:#fff}
.nav .btn{left:940px;top:13px;width:110px;height:37px;box-shadow:0 2px 6px rgba(0,0,0,.2)}
/* hero */
.hero{top:97px;height:627px;background:linear-gradient(180deg,#1c4f73 0%,#3c86b3 35%,#2f9fd0 60%,#1679b4 100%)}
.hero .shade{position:absolute;inset:0;background:linear-gradient(90deg,rgba(20,40,60,.35),rgba(0,0,0,0) 40%)}
.hero h2{position:absolute;top:80px;width:100%;text-align:center;color:#fff;font-weight:500;font-size:36px}
.hero h1{position:absolute;top:136px;width:100%;text-align:center;color:#fff;font-weight:600;font-size:66px;line-height:84px}
.hero p{position:absolute;top:316px;left:240px;width:720px;text-align:center;color:#fff;font-size:15px;line-height:24px}
.hero .btn{left:524px;top:373px;width:152px;height:34px;background:#fff;color:var(--ink);font-size:11px}
.filters{position:absolute;left:260px;top:518px;width:680px;height:85px;background:rgba(15,35,55,.55);border-radius:6px}
.filter{position:absolute;top:20px;color:#fff;font-size:15px;font-weight:600}
.select{margin-top:6px;width:148px;height:28px;background:#fff;border-radius:4px;color:#555;font-size:6px;font-weight:400;padding:10px 8px;position:relative}
.select::after{content:"⌄";position:absolute;right:8px;top:4px;font-size:10px}
.filters .btn{left:555px;top:24px;width:110px;height:36px;background:#fff;color:var(--ink)}
/* who */
.who{top:724px;height:653px}
.h-sec{font-size:36px;font-weight:600}
.who .h-sec{position:absolute;left:150px;top:92px}
.who .sub{position:absolute;left:150px;top:145px;font-size:24px;line-height:31px;width:600px}
.who .btn{left:930px;top:142px;width:100px;height:37px;font-size:10px;font-weight:500;font-family:Georgia,serif}
.tabs{position:absolute;left:150px;top:244px;width:355px;height:32px;border-radius:16px;background:#f2f4f7;display:flex;align-items:center;font-size:14px}
.tabs span{padding:0 18px;border-right:1px solid #bbb}
.tabs span:last-child{border:0;color:var(--blue);font-weight:500}
.stat{position:absolute;top:306px;text-align:center;font-size:12px;line-height:14px}
.stat b{display:block;font-size:36px;line-height:44px;color:var(--blue);font-weight:600}
.who .body{position:absolute;left:150px;top:443px;width:225px;font-size:12px;line-height:21px}
/* services */
.services{top:1377px;height:768px;background:radial-gradient(ellipse at 50% 40%,#1d5870 0%,#0f3546 60%,#0a2431 100%)}
.center-title{position:absolute;width:100%;text-align:center}
.services .t{top:52px;color:#fff}
.services .s{top:100px;color:#fff;font-size:22px}
.svc-img{position:absolute;top:176px;width:287px;height:340px;border-radius:8px;border:2px solid rgba(255,255,255,.6)}
.svc-info{position:absolute;top:528px;width:287px;height:93px;background:rgba(255,255,255,.15);border-radius:6px;color:#fff;padding:12px 14px}
.svc-info h3{font-size:19px;font-weight:500}
.svc-info p{font-size:11px;line-height:19px;margin-top:4px;color:#dce6ec}
.get{position:absolute;left:10px;bottom:10px;width:265px;height:36px;background:rgba(0,0,0,.45);border-radius:6px;color:#fff;font-size:11px;padding:10px 16px}
.get em{position:absolute;right:6px;top:4px;width:28px;height:28px;background:#fff;border-radius:5px;color:#000;font-style:normal;text-align:center;line-height:28px;font-size:16px}
.circ{position:absolute;width:32px;height:32px;border-radius:50%;border:1.5px solid #fff;color:#fff;text-align:center;line-height:29px;font-size:16px}
.track{position:absolute;left:243px;top:687px;width:733px;height:2px;background:#cfd8dd}
.count{position:absolute;left:990px;top:670px;color:#fff;font-size:24px}
.count small{font-size:14px}
/* work */
.work{top:2145px;height:788px}
.work .t{top:96px}
.work .s{top:139px;font-size:22px}
.side{position:absolute;top:262px;width:160px;height:283px;border-radius:10px;box-shadow:0 6px 18px rgba(0,0,0,.3)}
.cap{position:absolute;bottom:12px;color:#fff;font-size:12px;width:100%;text-align:center}
.main{position:absolute;left:415px;top:207px;width:372px;height:390px;border-radius:12px;box-shadow:0 12px 30px rgba(0,0,0,.35)}
.dot{position:absolute;top:392px;width:20px;height:20px;border-radius:50%;background:#222;color:#fff;text-align:center;line-height:20px;font-size:10px}
.shadow{position:absolute;left:300px;top:650px;width:600px;height:60px;background:radial-gradient(ellipse,rgba(0,0,0,.25),rgba(0,0,0,0) 70%)}
.work .btn{left:541px;top:665px;width:119px;height:33px;border-radius:4px;font-size:11px}
/* testimonials */
.clients{top:2933px;height:559px;background:linear-gradient(180deg,#1e3a22 0%,#2e5a3a 30%,#1f6b8f 60%,#134b6e 100%)}
.clients .t{top:75px;color:#fff}
.tcard{position:absolute;top:189px;width:291px;height:291px;background:#fff;border-radius:8px;text-align:center;padding-top:12px}
.avatar{width:110px;height:110px;border-radius:50%;margin:0 auto;border:3px solid #d0d6de;background:radial-gradient(circle at 50% 40%,#c9ced6,#8d96a3)}
.tcard h4{font-size:20px;font-weight:500;line-height:26px;margin-top:12px}
.tcard p{font-size:8.5px;line-height:15px;color:#333;padding:0 20px;margin-top:10px}
.stars{margin-top:8px;font-size:15px;color:var(--star)}
.stars small{color:#333;font-size:9px;margin-left:8px}
/* contact */
.contact{top:3492px;height:799px}
.contact .t{top:98px;font-size:28px;font-weight:600}
.cbox{position:absolute;left:150px;top:182px;width:900px;height:524px;border:1px solid #e0e3e8;border-radius:6px;box-shadow:0 4px 16px rgba(0,0,0,.08)}
.cbox h3{position:absolute;left:354px;top:30px;font-size:32px;font-weight:400}
.field label{position:absolute;left:356px;font-size:11px;color:var(--muted)}
.field div{position:absolute;left:356px;width:500px;height:40px;border:1px solid #b9c0ca;border-radius:10px;background:#f7f8fa}
.cbox .btn{left:354px;top:436px;width:504px;height:38px;font-size:11px}
/* footer */
.footer{top:4291px;height:408px;background:var(--navy);color:#fff}
.footer .brand{left:150px;top:124px;font-size:28px;color:#fff}
.footer .lead{position:absolute;left:150px;top:186px;font-size:14px;line-height:24px;width:360px}
.footer .social{position:absolute;left:150px;top:256px;gap:16px}
.footer .social span{width:32px;height:32px}
.fcol{position:absolute;top:98px}
.fcol h5{font-size:19px;font-weight:500;margin-bottom:16px}
.fcol li{list-style:none;font-size:11px;line-height:24px}
.rule{position:absolute;left:150px;top:366px;width:900px;height:1px;background:#3a4356}
.copy{position:absolute;top:378px;font-size:10px;color:#c9ced8}
</style>
</head>
<body>

<header class="topbar">
  <div class="abs hours">Monday – Friday: 8:00 AM – 9:00 PM</div>
  <div class="social"><span></span><span></span><span></span><span></span></div>
</header>

<header class="nav">
  <div class="brand"><i></i>Kalmenstrand</div>
  <ul><li>Home</li><li>About Us</li><li>What We Offer</li><li>Gallery</li><li>Testimonials</li></ul>
  <a class="btn btn-blue">Contact Us</a>
</header>

<section class="hero" role="img" aria-label="Modern villa terrace with sun loungers beside an infinity pool overlooking the sea">
  <div class="shade"></div>
  <h2>From Dream To Reality</h2>
  <h1>Transform Your Garden<br>With A Premium Pool</h1>
  <p>Custom-Designed Swimming Pools And Spas That Turn Your Backyard Into A Space Of Life, Relaxation, And Luxury</p>
  <a class="btn">"Explore Our Pools</a>
  <div class="filters">
    <div class="filter" style="left:22px">Pool Shape<div class="select">Select Pool Shape</div></div>
    <div class="filter" style="left:198px">Muinim Depth (Feet)<div class="select">Select Shallow End</div></div>
    <div class="filter" style="left:378px">Pool Shape<div class="select">Select Pool Shape</div></div>
    <a class="btn">Reset Filters</a>
  </div>
</section>

<section class="who">
  <h2 class="h-sec">Who We Are</h2>
  <p class="sub">Crafting Custom Pools With Precision, Passion, And A Personal Touch</p>
  <a class="btn btn-blue">Learn More</a>
  <div class="tabs"><span>Our History</span><span>Our Mission</span><span>Our Vision</span></div>
  <div class="stat" style="left:150px"><b>20+</b>years of<br>experience</div>
  <div class="stat" style="left:266px"><b>99%</b>clients<br>satisfaction</div>
  <p class="body">Kalmenstrand Is Dedicated To Creating High-Quality Swimming Pools And Spa Solutions For Your Home. We Combine Expertise, Innovation, And Aesthetics To Deliver Exceptional Outdoor Experiences.</p>
  <div class="photo" style="left:378px;top:306px;width:240px;height:257px;background:linear-gradient(180deg,#5d7a52,#3f8bb4 55%,#2a6f9a)" role="img" aria-label="Backyard pool with ladder surrounded by flower beds"></div>
  <div class="photo" style="left:685px;top:204px;width:365px;height:359px;background:linear-gradient(160deg,#6f8a5a,#8fb7a8 35%,#3fb0cf 60%,#a69880)" role="img" aria-label="Freeform pool with stone edging and pergola"></div>
</section>

<section class="services">
  <h2 class="center-title h-sec t">Our Services</h2>
  <p class="center-title s">Kalmenstrand Is Dedicated To Creating High-Quality Swimming Pools</p>
  <div class="svc-img photo" style="left:150px;background:linear-gradient(180deg,#4d6a3c,#2f7fa0 55%,#8a8070)" role="img" aria-label="Custom pool with stone spa">
    <div class="get">Get Now This Service<em>→</em></div>
  </div>
  <div class="svc-img photo" style="left:456px;background:linear-gradient(180deg,#bcd9ea,#5fb3dc 50%,#7a5a3c)" role="img" aria-label="Person relaxing in a lounge chair by a pool"></div>
  <div class="svc-img photo" style="left:762px;background:linear-gradient(180deg,#2f8fd0,#3f6fa5 50%,#6fb4d8)" role="img" aria-label="Technician servicing pool equipment"></div>
  <div class="svc-info" style="left:150px"><h3>Custom Swimming Pools</h3><p>Design And Installation Tailored To Your Space And Lifestyle</p></div>
  <div class="svc-info" style="left:456px"><h3>Spas &amp; Wellness</h3><p>Relaxing Spa Solutions For Ultimate Home Comfort</p></div>
  <div class="svc-info" style="left:762px"><h3>Pool Maintenance &amp; Support</h3><p>Professional Support To Keep Your Pool Perfect Year-Round.</p></div>
  <div class="circ" style="left:149px;top:672px">‹</div>
  <div class="circ" style="left:195px;top:672px">›</div>
  <div class="track"></div>
  <div class="count">01/ <small>02</small></div>
</section>

<section class="work">
  <h2 class="center-title h-sec t">Our Work</h2>
  <p class="center-title s">See How We Transform Gardens Into Stunning Pool Areas</p>
  <div class="side photo" style="left:271px;background:linear-gradient(180deg,#b8b8b0,#5fa6c6 50%,#2e6f90)" role="img" aria-label="Above ground pool"><div class="cap">Above Ground Pools</div></div>
  <div class="side photo" style="left:770px;background:linear-gradient(180deg,#b8b8b0,#5fa6c6 50%,#2e6f90)" role="img" aria-label="Above ground pool"><div class="cap">Above Ground Pools</div></div>
  <div class="main photo" style="background:linear-gradient(180deg,#6a8560,#4b7a5a 30%,#3a86b6 60%,#2a5f80)" role="img" aria-label="Backyard pool with flowers and ladder"><div class="cap" style="font-size:13px;bottom:20px">Above Ground Pools</div></div>
  <div class="dot" style="left:215px">‹</div>
  <div class="dot" style="left:953px">›</div>
  <div class="shadow"></div>
  <a class="btn btn-blue">View Gallery</a>
</section>

<section class="clients" role="img" aria-label="Garden pool with flowers in the background">
  <h2 class="center-title h-sec t">What Our Clients Say</h2>
  <div class="tcard" style="left:150px"><div class="avatar" role="img" aria-label="Client portrait"></div><h4>Linnea B.,<br>Universitätsstudentin</h4><p>Schnell, Präzise Und Hat Mich Wirklich Zum Nachdenken Gebracht! Ich War Überrascht, Wie Detailliert Die Punkteanalyse War</p><div class="stars">★★★★★<small>4.5</small></div></div>
  <div class="tcard" style="left:454px"><div class="avatar" role="img" aria-label="Client portrait"></div><h4>Johan M.,<br>Arbeitssuchender</h4><p>Das Design War Klar Und Der Test Wirkte Professionell. Ich Habe Meine Ergebnisse Sofort Erhalten – Sehr Aufschlussreich!"</p><div class="stars">★★★★★<small>4.5</small></div></div>
  <div class="tcard" style="left:758px"><div class="avatar" role="img" aria-label="Client portrait" style="background:radial-gradient(circle at 50% 40%,#e6c24a,#b38a1f)"></div><h4>Maja S.,<br>Wirtschaftsanalystin</h4><p>Ich Habe Den Test Nur Zum Spaß Gemacht, Habe Aber Letztendlich Viel Über Meine Stärken Gelernt. Sehr Empfehlenswert.</p><div class="stars">★★★★★<small>4.5</small></div></div>
</section>

<section class="contact">
  <h2 class="center-title t">Start Your Project Today</h2>
  <div class="cbox">
    <div class="photo" style="left:0;top:0;width:312px;height:524px;border-radius:6px 0 0 6px;background:linear-gradient(160deg,#7a8a6a,#1f5a78 35%,#0f3e5a 70%,#2a6a86)" role="img" aria-label="Pool with waterslide and stone edge"></div>
    <h3>Contact Us</h3>
    <div class="field"><label style="top:96px">Name</label><div style="top:118px"></div></div>
    <div class="field"><label style="top:180px">Email</label><div style="top:202px"></div></div>
    <div class="field"><label style="top:264px">Addess</label><div style="top:286px"></div></div>
    <div class="field"><label style="top:343px">Phone Number</label><div style="top:365px"></div></div>
    <a class="btn btn-blue">Submit</a>
  </div>
</section>

<footer class="footer">
  <div class="brand"><i></i>Kalmenstrand</div>
  <p class="lead">Lorem Ipsum Dolor Amet Consectetur. Mauris Enim Dapibus Mauris Leo</p>
  <div class="social"><span></span><span></span><span></span><span></span></div>
  <div class="fcol" style="left:590px"><h5>Services</h5><ul><li style="line-height:14px;margin-bottom:8px">Custom Swimming<br>Pools</li><li style="line-height:14px;margin-bottom:8px">Spas &amp; Wellness</li><li style="line-height:14px">Pool Maintenance &amp;<br>Support</li></ul></div>
  <div class="fcol" style="left:770px"><h5>Used Full Links</h5><ul><li>Home</li><li>About Us</li><li>What We Offer</li><li>Gallery</li><li>Testimonials</li></ul></div>
  <div class="fcol" style="left:968px"><h5>Legal</h5><ul><li style="margin-bottom:8px">Terms Of Use</li><li style="margin-bottom:8px">Privacy Policy</li><li>Cookie Policy</li></ul></div>
  <div class="rule"></div>
  <div class="copy" style="left:150px">Copyright © 2025 All Right Reserved</div>
  <div class="copy" style="left:728px">Privacy Policy</div>
  <div class="copy" style="left:834px">Terms Of Service</div>
  <div class="copy" style="left:958px">Cookies Settings</div>
</footer>

</body>
</html>
```